New flavour! New packaging for Velocity Energy Drink!

We need a new packaging designed to show off our new grape flavored energy drink! It will require box design with matching sachets!

Established in 2018 we are a fully Australian owned and operated business that started out with 2 gamers that got sick and tired of sugary energy drinks OR expensive powder from the USA.

We are an energy drink in the esports and gaming space. Our new product is an energy drink in powder in boxes of 30 sachets (please see attached for product example)

Please see example 1 and 2 for our competitors product. We would ideally like to go a bit more minimalist than them but still have a great color pop on black backing.

Target Market(s)

Gamer's and esports athletes between the ages or 18-30

Font styles to use
Sans Serif
Other font styles liked:
• Helvetica

Colors
886aae
ffffff

Requirements
Must have
• Black base/background.
• Vibrant purple N in the Velocity Logo.
• Same or slightly different shades of purple for some text and highlights.
• Black, white and some shades of a vibrant purple (for the grape flavor)
• ingredients list (may need to be reformatted to suit)
• Please see attached for legislative requirements on the box and sachets.
Nice to have
• minimalist design but enough to be eye catching and somewhat playful
• Twitter: @VLCT_FUEL
• Instagram: @VLCT_FUEL
• Facebook: @VLCTFUEL
Should not have
• OTHER COLORS.
• Overly complex designs.

```html
<!DOCTYPE html>
<html lang="en">
<head>
<meta charset="UTF-8">
<title>Velocity Energy Drink – Grape Sachet</title>
<link rel="stylesheet" href="https://fonts.googleapis.com/css2?family=Archivo+Black&family=Archivo:wght@700;800&display=swap">
<style>
  :root {
    --page-bg: #f7f7f7;
    --seal-purple: #372b4d;
    --deep-purple: #3a2e55;
    --mid-purple: #574583;
    --brand-purple: #886aae;
    --light-lilac: #b9afd4;
    --mist: #e9e7f0;
    --white: #ffffff;
    --ink: #2a1f2b;
  }
  html, body {
    margin: 0;
    width: 900px;
    height: 1200px;
    overflow: hidden;
    background: var(--page-bg);
  }
  .canvas {
    position: relative;
    width: 900px;
    height: 1200px;
  }
  .sachet {
    position: absolute;
    left: 270px;
    top: 119px;
    width: 358px;
    height: 963px;
  }
  .sachet-shape {
    position: absolute;
    inset: 0;
    width: 100%;
    height: 100%;
  }
  .rotated {
    position: absolute;
    transform: translate(-50%, -50%) rotate(-90deg);
    white-space: nowrap;
    text-align: center;
  }
  .brand-name {
    left: 128px;
    top: 494px;
    width: 690px;
    font-family: "Archivo Black", "Archivo", sans-serif;
    font-size: 128px;
    line-height: 1;
    color: var(--white);
    letter-spacing: 2px;
  }
  .product-type {
    left: 195px;
    top: 319px;
    width: 306px;
    font-family: "Archivo", sans-serif;
    font-weight: 800;
    font-size: 19px;
    letter-spacing: 5px;
    line-height: 1;
    color: var(--white);
  }
  .flavour-block {
    left: 284px;
    top: 472px;
    width: 420px;
    font-family: "Archivo", sans-serif;
    font-weight: 800;
    color: var(--ink);
  }
  .flavour-name {
    font-size: 33px;
    letter-spacing: 5px;
    line-height: 1;
    margin-bottom: 12px;
  }
  .flavour-detail {
    font-size: 17px;
    letter-spacing: 6px;
    line-height: 1.3;
  }
  .flavour-tagline {
    font-size: 17px;
    letter-spacing: 6px;
    line-height: 1.3;
    margin-top: 4px;
  }
</style>
</head>
<body>
<div class="canvas">
  <div class="sachet">
    <svg class="sachet-shape" viewBox="0 0 358 963" role="img" aria-label="Grape sachet body with fizzy bubbles and halftone dot sparkle">
      <defs>
        <linearGradient id="bodyFade" x1="0" y1="0" x2="1" y2="0">
          <stop offset="0" stop-color="#3a2e55"/>
          <stop offset="0.45" stop-color="#574583"/>
          <stop offset="0.7" stop-color="#8f80b8"/>
          <stop offset="1" stop-color="#e9e7f0"/>
        </linearGradient>
      </defs>
      <rect x="0" y="0" width="358" height="57" fill="#372b4d"/>
      <rect x="0" y="906" width="358" height="57" fill="#372b4d"/>
      <rect x="22" y="57" width="318" height="849" fill="url(#bodyFade)"/>
    </svg>

    <div class="rotated brand-name">VELOCITY</div>
    <div class="rotated product-type">ENERGY DRINK</div>
    <div class="rotated flavour-block">
      <div class="flavour-name">GRAPE FLAVOUR</div>
      <div class="flavour-detail">WITH GINSENG &amp;<br>CAFFEINE</div>
      <div class="flavour-tagline">FOR GAMERS, BY GAMERS</div>
    </div>
  </div>
</div>
</body>
</html>
```